Vereins Website
Zielgruppe
Webiste für den Verein 'Katzenhain Oberlau' (details siehe Anhang).
Ziel der Website:
- Sponsoren finden
- Vereinsmitglieder finden & Interessen bündeln.
Aufgabenstellung
Die Webiste sollt aufgeräumt, übersichtlich und freundlich wirken.

```html
<!DOCTYPE html>
<html lang="de">
<head>
<meta charset="utf-8">
<title>Verein Katzenhain Oberlau</title>
<link href="https://fonts.googleapis.com/css2?family=Montserrat:wght@400;500;600;700&family=Roboto:wght@500;700&display=swap" rel="stylesheet">
<style>
:root{
  --orange:#f2a33a;
  --orange-text:#ef9a2c;
  --text:#555;
  --dark:#2b2b2b;
  --cream:#fbf2ea;
  --footer:#3e2f26;
  --line:#c9c9c9;
  --white:#fff;
}
*{box-sizing:border-box;margin:0;padding:0}
html,body{width:1200px;height:3375px;overflow:hidden}
body{position:relative;font-family:'Montserrat',sans-serif;color:var(--text);background:var(--white)}
.abs{position:absolute}
.nav{left:0;top:0;width:1200px;height:62px;background:#fafafa}
.brand{left:258px;top:14px;display:flex;align-items:center;gap:8px;font-size:12px;font-weight:700;color:var(--dark);line-height:1.1;width:90px}
.brand-dot{width:18px;height:18px;border-radius:50%;background:var(--orange);flex:none}
.nav-link{top:26px;font-size:10.5px;font-weight:500;color:var(--dark);letter-spacing:.3px}
.photo{left:0;width:1200px}
.hero{top:62px;height:511px;background:linear-gradient(180deg,#6f7f4a 0%,#8fa55a 45%,#7fa240 75%,#6a8c32 100%)}
.hero-title{left:0;width:1200px;top:240px;text-align:center;color:var(--white);font-weight:700;font-size:41px;line-height:44px;text-shadow:0 2px 6px rgba(0,0,0,.35)}
.btn{background:var(--orange);color:var(--white);font-weight:600;text-align:center;border-radius:2px}
.hero-btn{top:368px;height:35px;line-height:35px;font-size:14.5px}
.section-title{left:0;width:1200px;text-align:center;font-family:'Roboto',sans-serif;font-weight:500;font-size:29px;color:var(--dark);display:flex;justify-content:center;align-items:center;gap:8px}
.bone{width:46px;height:24px}
.about-text{left:258px;width:686px;top:752px;font-size:15.5px;line-height:17.6px;text-align:justify}
.about-text p+p{margin-top:17px}
.band-care{top:1104px;height:397px;background:linear-gradient(100deg,#a9b0ae 0%,#c2c7c5 35%,#3c4a66 55%,#d9b782 75%,#8cb155 100%)}
.label{font-size:11.5px;font-weight:600;color:var(--orange-text);text-transform:uppercase}
.member-copy{left:68px;top:1832px;width:464px;font-size:12.3px;line-height:18.3px}
.member-copy p{text-align:justify;margin-top:8px}
.member-copy p+p{margin-top:18px}
.member-copy strong{display:block;margin-top:18px;color:var(--dark);font-weight:600}
.field{border:1px solid var(--line);background:var(--white);font-size:10px;color:#999;padding:0 9px;display:flex;align-items:center;font-family:Arial,sans-serif}
.form-btn{height:27px;line-height:27px;font-size:11px;font-weight:500}
.sponsor-band{left:0;top:2269px;width:1200px;height:299px;background:var(--cream)}
.sponsor-sub{left:0;width:1200px;top:2356px;text-align:center;font-size:12px;font-weight:500;color:var(--orange-text)}
.sponsor{top:2421px;height:83px;background:var(--white);display:flex;align-items:center;justify-content:center;font-size:13px;font-weight:700;color:var(--dark);text-align:center}
.sponsor.slot{background:var(--orange);font-weight:500;font-size:11.5px;line-height:14px;color:var(--dark)}
.donate{font-size:12.2px;line-height:21px;color:var(--dark)}
.donate b{font-weight:700}
.pay{font-size:11px;font-weight:700;color:var(--dark);display:flex;align-items:center;justify-content:center}
.band-hands{top:2871px;height:255px;background:linear-gradient(180deg,#8a5a36 0%,#a56b3c 40%,#9b7a55 70%,#6f7f4a 100%)}
.band-title{left:0;width:1200px;top:2983px;text-align:center;color:var(--white);font-weight:700;font-size:30px;text-shadow:0 2px 6px rgba(0,0,0,.4)}
.footer{left:0;top:3338px;width:1200px;height:37px;background:var(--footer);color:var(--white);text-align:center;line-height:37px;font-size:11px}
</style>
</head>
<body>

<header>
  <div class="abs nav"></div>
  <div class="abs brand"><span class="brand-dot"></span><span>Katzenhain Oberlau</span></div>
  <a class="abs nav-link" style="left:716px">MITGLIED</a>
  <a class="abs nav-link" style="left:798px">SPONSOR</a>
  <a class="abs nav-link" style="left:880px">KONTAKT</a>
</header>

<section>
  <div class="abs photo hero" role="img" aria-label="Foto: Hund auf einer sonnigen Wiese mit Bäumen"></div>
  <h1 class="abs hero-title">Lorem ipsum dolor sit amet mit<br>Verein Katzenhain Oberlau</h1>
  <div class="abs btn hero-btn" style="left:389px;width:183px">MITGLIED WERDEN</div>
  <div class="abs btn hero-btn" style="left:630px;width:186px">SPONSOR WERDEN</div>
</section>

<svg width="0" height="0" style="position:absolute">
  <symbol id="bone" viewBox="0 0 46 24">
    <g fill="none" stroke="#f2a33a" stroke-width="4">
      <path d="M12 7 H34 A6 6 0 1 1 38 12 A6 6 0 1 1 34 17 H12 A6 6 0 1 1 8 12 A6 6 0 1 1 12 7 Z"/>
    </g>
  </symbol>
</svg>

<section>
  <h2 class="abs section-title" style="top:680px"><svg class="bone"><use href="#bone"/></svg>Verein Katzenhain Oberlau</h2>
  <div class="abs about-text">
    <p>Nach dem Vorbild von Eiken möchten wir in Oberlau eine eingezäunte Hundespielwiese auf die Beine stellen und damit das Wohlergehen der Hunde fördern.Auf der eingezäunten Wiese können die Hunde ohne Leinenzwang spielen, sich austoben und sozialisieren.Gleichzeitig schafft dies einen Raum, in dem sich die Hundehalter treffen und austauschen können.</p>
    <p>Ein Begegnungsort für die ganze Region, von dem alle profitieren.</p>
  </div>
</section>

<div class="abs photo band-care" role="img" aria-label="Foto: Person streichelt einen hellen Hund im Gras"></div>

<section>
  <h2 class="abs section-title" style="top:1740px"><svg class="bone"><use href="#bone"/></svg>Werden Sie Vereinsmitglied</h2>
  <div class="abs member-copy">
    <div class="label">Projekt unterstützen und Vereinsmitglied werden</div>
    <p>Lorem ipsum dolor sit amet, eu sed nulla imperdiet complectitur, dico philosophia eu vel, dicunt maluisset imperdiet et eos. At usu verterem partiendo consetetur, id nullam laboramus nec. Et paulo nobis integre sit, qui ludus option periculis id.</p>
    <p>Fierent incorrupte no qui. Vide invenire mediocritatem duo et.Everti appetere eos et. Vel viris verterem ex, mollis iriure feugiat eum eu. Ea pro corpora percipitur, brute nemore ei eum. Iuvaret partiendo laboramus te pri, in per enim nominavi, eligendi inciderint ea vix. Wisi erat an ius.Id feugiat recteque vim, ex oratio epicuri elaboraret duo.</p>
    <strong>Eine Vereinsmitgliedschaft ist derzeit noch kostenlos.<br>Sie unterstützen den Verein damit ideell.</strong>
  </div>
  <div class="abs label" style="left:743px;top:1832px">Anmeldeformular</div>
  <div class="abs field" style="left:743px;top:1869px;width:255px;height:27px">Name</div>
  <div class="abs field" style="left:743px;top:1917px;width:255px;height:27px">Vorname</div>
  <div class="abs field" style="left:743px;top:1965px;width:255px;height:27px">Strasse / Nr.</div>
  <div class="abs field" style="left:743px;top:2014px;width:58px;height:27px">PLZ</div>
  <div class="abs field" style="left:743px;top:2061px;width:255px;height:27px">Ort</div>
  <div class="abs field" style="left:743px;top:2109px;width:255px;height:27px">E-Mail Adresse</div>
  <div class="abs btn form-btn" style="left:743px;top:2158px;width:73px">SENDEN</div>
</section>

<section>
  <div class="abs sponsor-band"></div>
  <h2 class="abs section-title" style="top:2314px"><svg class="bone"><use href="#bone"/></svg>Werden Sie Sponsor</h2>
  <div class="abs sponsor-sub">HELFEN SIE UNS DIESES PROJEKT ZU VERWIRKLICHEN</div>
  <div class="abs sponsor" style="left:98px;width:125px">Pfotenküche</div>
  <div class="abs sponsor slot" style="left:326px;width:96px">HIER KÖNNTE<br>IHR LOGO<br>STEHEN</div>
  <div class="abs sponsor" style="left:536px;width:105px">Napfland</div>
  <div class="abs sponsor" style="left:752px;width:126px">Treuhund</div>
  <div class="abs sponsor" style="left:981px;top:2434px;width:125px;height:55px">Kronenfutter</div>
</section>

<section>
  <div class="abs donate" style="left:168px;top:2601px">
    <div class="label">Für Firmen spenden</div>
    <div><b>SPENDENKONTO:</b> KATZENHAIN OBERLAU</div>
    <div><b>IBAN:</b> 98 00000 00000 00000 9</div>
    <div><b>BIC:</b> 6553873</div>
  </div>
  <div class="abs donate" style="left:774px;top:2601px">
    <div class="label">Für private Spenden</div>
    <div><b>SPENDENKONTO:</b> KATZENHAIN OBERLAU</div>
    <div><b>IBAN:</b> 98 00000 00000 00000 9</div>
    <div><b>BIC:</b> 6553873</div>
  </div>
  <div class="abs pay" style="left:773px;top:2715px;width:93px;height:26px;background:#fff">Postkasse</div>
  <div class="abs pay" style="left:880px;top:2705px;width:46px;height:45px;font-size:9px">Zahlpunkt</div>
  <div class="abs pay" style="left:773px;top:2750px;width:50px;height:46px;font-size:10px">Netzbeutel</div>
  <div class="abs pay" style="left:836px;top:2762px;width:93px;height:24px;background:var(--orange);font-size:7.5px;font-weight:500">EINZAHLUNGSSCHEIN</div>
</section>

<section>
  <div class="abs photo band-hands" role="img" aria-label="Foto: Hundepfote in einer Hand auf einer Wiese"></div>
  <h2 class="abs band-title">Wir freuen uns auf Ihre Anregungen &amp; Ideen</h2>
  <div class="abs field" style="left:288px;top:3177px;width:306px;height:27px">Name</div>
  <div class="abs field" style="left:288px;top:3212px;width:306px;height:28px">E-Mail Adresse</div>
  <div class="abs field" style="left:638px;top:3177px;width:307px;height:63px;align-items:flex-start;padding-top:8px">Ihr Text</div>
  <div class="abs" style="left:288px;top:3250px;width:9px;height:9px;border:1px solid var(--line)"></div>
  <div class="abs" style="left:304px;top:3249px;font-size:9px;color:#777">Kopie an meine E-Mail Adresse</div>
  <div class="abs btn form-btn" style="left:288px;top:3279px;width:66px">SENDEN</div>
</section>

<footer class="abs footer">info@katzenhain-oberlau.ch</footer>
</body>
</html>
```